sticker for cleaning products

it is in the bottle. products are bio-cleaner. Toilet Cleaner - yellow Sanitary Cleaner - orange Glass Cleaner - light blue All purpose cleaner - green Hand Soap - cream Detergent - olive Detergent - rose bottles is used VARIO: https://glasvormenhaus.de/katalog/#Vario shape of the sticker is not geometric. It's something like a cloud / leaf / drop / ?? the sticker has an inner space with only the product name and color. the sticker has an outer space. here we want to mark out "powered by QUENSOLI" (our company name, find logo attached)

```html
<!DOCTYPE html>
<html lang="de">
<head>
<meta charset="utf-8">
<title>QUENSOLI Refill – Produktetiketten</title>
<link rel="stylesheet" href="https://fonts.googleapis.com/css2?family=Roboto+Condensed:wght@400;700&display=swap">
<style>
  :root {
    --paper: #ffffff;
    --ink: #2b2b2b;
    --label-white: #ffffff;

    --green-main: #4a8f1a; --green-light: #7db833; --green-dark: #2a700e; --green-band: #2a6232;
    --yellow-main: #efc70a; --yellow-light: #f7e21b; --yellow-dark: #e5a00b; --yellow-band: #ef8a3e;
    --orange-main: #ef8c0e; --orange-light: #f8b819; --orange-dark: #e05a0a; --orange-band: #e22129;
    --blue-main: #1f7fc8; --blue-light: #4aa8de; --blue-dark: #0a52a5; --blue-band: #075779;
    --olive-main: #86884c; --olive-light: #aeb27e; --olive-dark: #5f6a2a; --olive-band: #6a6e33;
    --cream-main: #f2ea91; --cream-light: #f7f1bc; --cream-dark: #ece175; --cream-band: #fcea00; --cream-text: #3a3a3a;
    --rose-main: #d04b84; --rose-light: #e680ae; --rose-dark: #b82a62; --rose-band: #e20a7b;
  }
  html, body { margin: 0; padding: 0; overflow: hidden; background: var(--paper); }
  .sheet { display: block; width: 1200px; height: 848px; }
  .product-name { font-family: "Roboto Condensed", "Arial Narrow", sans-serif; font-weight: 700; font-size: 40px; }
  .brand-name { font-family: "Roboto Condensed", "Arial Narrow", sans-serif; font-weight: 400; font-size: 16px; letter-spacing: 7px; fill: var(--ink); }
  .brand-dot { fill: none; stroke: var(--ink); stroke-width: 3; }
  .sheen { fill: #ffffff; opacity: .09; }
  .leaf-area { opacity: .35; }

  .sticker--green  { --c-main: var(--green-main);  --c-light: var(--green-light);  --c-dark: var(--green-dark);  --c-band: var(--green-band);  --c-text: var(--label-white); }
  .sticker--yellow { --c-main: var(--yellow-main); --c-light: var(--yellow-light); --c-dark: var(--yellow-dark); --c-band: var(--yellow-band); --c-text: var(--label-white); }
  .sticker--orange { --c-main: var(--orange-main); --c-light: var(--orange-light); --c-dark: var(--orange-dark); --c-band: var(--orange-band); --c-text: var(--label-white); }
  .sticker--blue   { --c-main: var(--blue-main);   --c-light: var(--blue-light);   --c-dark: var(--blue-dark);   --c-band: var(--blue-band);   --c-text: var(--label-white); }
  .sticker--olive  { --c-main: var(--olive-main);  --c-light: var(--olive-light);  --c-dark: var(--olive-dark);  --c-band: var(--olive-band);  --c-text: var(--label-white); }
  .sticker--cream  { --c-main: var(--cream-main);  --c-light: var(--cream-light);  --c-dark: var(--cream-dark);  --c-band: var(--cream-band);  --c-text: var(--cream-text); }
  .sticker--rose   { --c-main: var(--rose-main);   --c-light: var(--rose-light);   --c-dark: var(--rose-dark);   --c-band: var(--rose-band);   --c-text: var(--label-white); }

  .drop-rim   { fill: var(--c-light); }
  .drop-body  { fill: var(--c-main); }
  .drop-edge  { fill: var(--c-dark); }
  .name-band  { fill: var(--c-band); }
  .leaf-area  { fill: var(--c-dark); }
  .product-name { fill: var(--c-text); }
</style>
</head>
<body>
<svg class="sheet" viewBox="0 0 1200 848" xmlns="http://www.w3.org/2000/svg">
  <defs>
    <clipPath id="drop-clip">
      <path d="M268 0 C225 50 225 180 335 255 C400 300 425 370 422 425 C420 545 320 635 210 635 C95 635 0 540 0 420 C0 300 60 190 140 115 C190 65 230 30 268 0 Z"/>
    </clipPath>
    <g id="drop-art">
      <path class="drop-rim" d="M268 0 C225 50 225 180 335 255 C400 300 425 370 422 425 C420 545 320 635 210 635 C95 635 0 540 0 420 C0 300 60 190 140 115 C190 65 230 30 268 0 Z"/>
      <path class="drop-body" d="M268 0 C205 60 200 170 290 250 C370 330 420 400 410 470 C400 560 320 635 210 635 C95 635 0 540 0 420 C0 300 60 190 140 115 C190 65 230 30 268 0 Z"/>
      <path class="sheen" d="M140 200 C230 300 280 420 330 610 L290 640 C270 500 230 380 140 250 Z"/>
      <rect class="drop-edge" x="0" y="0" width="58" height="640" opacity=".55"/>
      <path class="drop-edge" d="M36 230 C62 330 60 460 34 560 L28 560 L28 230 Z"/>
    </g>
  </defs>

  <!-- Allzweckreiniger -->
  <g class="sticker sticker--green" transform="translate(125 91) scale(0.52)">
    <g clip-path="url(#drop-clip)">
      <use href="#drop-art"/>
      <rect class="name-band" x="83" y="0" width="60" height="640"/>
    </g>
    <ellipse class="leaf-area" role="img" aria-label="Blätter-Dekor" cx="225" cy="268" rx="65" ry="52"/>
    <text class="product-name" transform="translate(127 547) rotate(-90)">ALLZWECKREINIGER</text>
    <circle class="brand-dot" cx="268" cy="460" r="21"/>
    <text class="brand-name" x="272" y="505" text-anchor="middle">QUENSOLI</text>
  </g>

  <!-- WC Reiniger -->
  <g class="sticker sticker--yellow" transform="translate(376 91) scale(0.52)">
    <g clip-path="url(#drop-clip)">
      <use href="#drop-art"/>
      <rect class="name-band" x="83" y="0" width="60" height="640"/>
    </g>
    <ellipse class="leaf-area" role="img" aria-label="Blätter-Dekor" cx="225" cy="268" rx="65" ry="52"/>
    <text class="product-name" transform="translate(127 507) rotate(-90)">WC REINIGER</text>
    <circle class="brand-dot" cx="268" cy="460" r="21"/>
    <text class="brand-name" x="272" y="505" text-anchor="middle">QUENSOLI</text>
  </g>

  <!-- Sanitärreiniger -->
  <g class="sticker sticker--orange" transform="translate(634 103) scale(0.52)">
    <g clip-path="url(#drop-clip)">
      <use href="#drop-art"/>
      <rect class="name-band" x="83" y="0" width="60" height="640"/>
    </g>
    <ellipse class="leaf-area" role="img" aria-label="Blätter-Dekor" cx="225" cy="268" rx="65" ry="52"/>
    <text class="product-name" transform="translate(127 542) rotate(-90)">SANITÄRREINIGER</text>
    <circle class="brand-dot" cx="268" cy="460" r="21"/>
    <text class="brand-name" x="272" y="505" text-anchor="middle">QUENSOLI</text>
  </g>

  <!-- Glasreiniger -->
  <g class="sticker sticker--blue" transform="translate(892 97) scale(0.52)">
    <g clip-path="url(#drop-clip)">
      <use href="#drop-art"/>
      <rect class="name-band" x="83" y="0" width="60" height="640"/>
    </g>
    <ellipse class="leaf-area" role="img" aria-label="Blätter-Dekor" cx="225" cy="268" rx="65" ry="52"/>
    <text class="product-name" transform="translate(127 509) rotate(-90)">GLASREINIGER</text>
    <circle class="brand-dot" cx="268" cy="460" r="21"/>
    <text class="brand-name" x="272" y="505" text-anchor="middle">QUENSOLI</text>
  </g>

  <!-- Spülmittel -->
  <g class="sticker sticker--olive" transform="translate(140 443) scale(0.52)">
    <g clip-path="url(#drop-clip)">
      <use href="#drop-art"/>
      <rect class="name-band" x="83" y="0" width="60" height="640"/>
    </g>
    <ellipse class="leaf-area" role="img" aria-label="Blätter-Dekor" cx="225" cy="268" rx="65" ry="52"/>
    <text class="product-name" transform="translate(127 498) rotate(-90)">SPÜLMITTEL</text>
    <circle class="brand-dot" cx="268" cy="460" r="21"/>
    <text class="brand-name" x="272" y="505" text-anchor="middle">QUENSOLI</text>
  </g>

  <!-- Handseife -->
  <g class="sticker sticker--cream" transform="translate(391 437) scale(0.52)">
    <g clip-path="url(#drop-clip)">
      <use href="#drop-art"/>
      <rect class="name-band" x="83" y="0" width="60" height="640"/>
    </g>
    <ellipse class="leaf-area" role="img" aria-label="Blätter-Dekor" cx="225" cy="268" rx="65" ry="52"/>
    <text class="product-name" transform="translate(127 488) rotate(-90)">HANDSEIFE</text>
    <circle class="brand-dot" cx="268" cy="460" r="21"/>
    <text class="brand-name" x="272" y="505" text-anchor="middle">QUENSOLI</text>
  </g>

  <!-- Waschmittel -->
  <g class="sticker sticker--rose" transform="translate(645 437) scale(0.52)">
    <g clip-path="url(#drop-clip)">
      <use href="#drop-art"/>
      <rect class="name-band" x="83" y="0" width="60" height="640"/>
    </g>
    <ellipse class="leaf-area" role="img" aria-label="Blätter-Dekor" cx="225" cy="268" rx="65" ry="52"/>
    <text class="product-name" transform="translate(127 518) rotate(-90)">WASCHMITTEL</text>
    <circle class="brand-dot" cx="268" cy="460" r="21"/>
    <text class="brand-name" x="272" y="505" text-anchor="middle">QUENSOLI</text>
  </g>
</svg>
</body>
</html>
```